Design an Exhibition Poster for our Web Application

Our company develops and sells VaultLarkly, a web-based service that helps small businesses to test their web applications for security vulnerabilities.

You can see details of the service at the following page:

https://www.vaultlarkly.example/

We need a poster designed, to be used on an exhibition stand at a professional security conference.
Updates

Project Deadline Extended
Reason: The deadline for this project is being extended because we have, so far, received very few design submissions and they are generally not of the aesthetic quality we are looking for.

Target Market(s)

Tech startups and small / medium sized online businesses

Industry/Entity Type

Security

Requirements
Must have
• [1] Incorporate the VaultLarkly logo (see attached file).

[2] Use the text supplied by us (see attached file).

[3] Use a color scheme that matches the scheme used on our website.

[4] Project the visual theme of cyber security (or protection against cyber crime).
Nice to have
• This is part of a 2-poster set. The project for designing the other poster in the set is also being listed on ArtFolio today. Please look for the project entitled "Design an Exhibition Poster for our Software Product".

Preference will be given to designers who submit a pair of designs that harmonize with each other.

```html
<!DOCTYPE html>
<html lang="en">
<head>
<meta charset="utf-8">
<title>VaultLarkly – Security For Web Startups</title>
<link rel="stylesheet" href="https://fonts.googleapis.com/css2?family=Comfortaa:wght@400;700&family=Days+One&display=swap">
<style>
  :root {
    --band-dark: #383838;
    --band-green: #7f9a5b;
    --green-edge: #a3b784;
    --ink-light: #f4f2e8;
    --rule: #8a8a8a;
  }
  * { margin: 0; padding: 0; box-sizing: border-box; }
  html, body { width: 848px; height: 1200px; overflow: hidden; background: var(--band-green); }
  .poster {
    position: relative; width: 848px; height: 1200px; overflow: hidden;
    font-family: "Comfortaa", sans-serif; color: var(--ink-light);
  }
  .band { position: absolute; left: 0; width: 848px; }
  .band--dark { background: var(--band-dark); }
  .band--green { background: var(--band-green); }
  .band--green + .band--dark, .band--dark + .band--green { border-top: 2px solid var(--green-edge); }

  .header { top: 0; height: 108px; }
  .headline {
    position: absolute; top: 26px; width: 100%; text-align: center;
    font-family: "Days One", sans-serif; font-size: 39px; letter-spacing: 1px; font-weight: 400;
  }
  .header-rule { position: absolute; left: 71px; width: 707px; top: 86px; height: 1px; background: var(--rule); }

  .intro { top: 108px; height: 172px; }
  .intro-text {
    position: absolute; top: 52px; width: 100%; text-align: center;
    font-size: 24px; line-height: 34px;
  }

  .brand { top: 280px; height: 125px; }
  .brand-mark { position: absolute; left: 150px; top: 26px; width: 78px; height: 74px; background: var(--band-green); }
  .brand-name {
    position: absolute; left: 250px; top: 22px; font-size: 64px; font-weight: 700; line-height: 80px;
  }

  .features { top: 405px; height: 650px; }
  .feature { position: absolute; }
  .feature-icon { position: absolute; }
  .feature-text { position: absolute; font-size: 24px; line-height: 34px; }
  .feature-text strong { font-weight: 700; }

  .cta { top: 1055px; height: 96px; }
  .cta-icon { position: absolute; left: 152px; top: 22px; }
  .cta-text {
    position: absolute; left: 262px; top: 24px;
    font-family: "Days One", sans-serif; font-size: 38px; letter-spacing: 1px;
  }
  .footer { top: 1151px; height: 49px; }
</style>
</head>
<body>
<main class="poster">
  <header class="band band--dark header">
    <h1 class="headline">Security For Web Startups</h1>
    <div class="header-rule"></div>
  </header>

  <section class="band band--green intro">
    <p class="intro-text">Online website vulnerability scanning that tells<br>you exactly what needs fixing and how to to fix it.</p>
  </section>

  <section class="band band--dark brand">
    <div class="brand-mark"></div>
    <div class="brand-name">VaultLarkly</div>
  </section>

  <section class="band band--green features">
    <!-- Accessible -->
    <svg class="feature-icon" style="left:95px;top:45px" width="112" height="145" viewBox="0 0 112 145" aria-hidden="true">
      <circle cx="62" cy="48" r="36" fill="none" stroke="var(--ink-light)" stroke-width="16"/>
      <circle cx="62" cy="48" r="8" fill="var(--ink-light)"/>
      <rect x="0" y="76" width="48" height="16" rx="8" transform="rotate(-45 24 84)" fill="var(--ink-light)"/>
      <rect x="48" y="84" width="16" height="60" fill="var(--ink-light)"/>
      <rect x="64" y="104" width="18" height="12" fill="var(--ink-light)"/>
      <rect x="64" y="124" width="18" height="12" fill="var(--ink-light)"/>
    </svg>
    <p class="feature-text" style="left:225px;top:80px"><strong>Accessible:</strong> VaultLarkly runs in the<br>cloud and is accessible from<br>any computer, anywhere, any time.</p>

    <!-- Affordable -->
    <svg class="feature-icon" style="left:140px;top:228px" width="104" height="170" viewBox="0 0 104 170" aria-hidden="true">
      <g fill="var(--ink-light)" font-family="Comfortaa, sans-serif" font-weight="700" font-size="26">
        <text x="10" y="28">$</text><text x="2" y="66">$</text><text x="36" y="60">$</text><text x="66" y="66">$</text>
      </g>
      <path d="M6 124 Q52 68 98 124 Q86 114 75 124 Q63 114 52 124 Q40 114 29 124 Q18 114 6 124Z" fill="var(--ink-light)"/>
      <path d="M52 124 V158 Q52 168 42 168 Q33 168 33 158" fill="none" stroke="var(--ink-light)" stroke-width="7" stroke-linecap="round"/>
    </svg>
    <p class="feature-text" style="left:268px;top:287px"><strong>Affordable:</strong> VaultLarkly uses<br>a flexible pay-as-you-go<br>model that will fit any budget.</p>

    <!-- Simple -->
    <svg class="feature-icon" style="left:103px;top:438px" width="180" height="140" viewBox="0 0 180 140" aria-hidden="true">
      <g fill="none" stroke="var(--ink-light)">
        <circle cx="42" cy="82" r="26" stroke-width="20"/>
        <circle cx="42" cy="82" r="38" stroke-width="10" stroke-dasharray="12 11.9"/>
        <circle cx="110" cy="32" r="17" stroke-width="13"/>
        <circle cx="110" cy="32" r="25" stroke-width="8" stroke-dasharray="9 10.6"/>
        <circle cx="126" cy="104" r="20" stroke-width="15"/>
        <circle cx="126" cy="104" r="30" stroke-width="9" stroke-dasharray="10 11"/>
      </g>
    </svg>
    <p class="feature-text" style="left:299px;top:461px"><strong>Simple:</strong> Launch your scan<br>using a simple 3-step wizard<br>and we'll do the rest.</p>
  </section>

  <section class="band band--dark cta">
    <svg class="cta-icon" width="100" height="54" viewBox="0 0 100 54" aria-hidden="true">
      <path d="M4 20 H22 L62 4 V50 L22 34 H4Z" fill="var(--ink-light)"/>
      <path d="M14 34 L20 50 H30 L26 34Z" fill="var(--ink-light)"/>
      <g stroke="var(--ink-light)" stroke-width="4" stroke-linecap="round">
        <line x1="72" y1="14" x2="86" y2="6"/><line x1="74" y1="27" x2="92" y2="27"/><line x1="72" y1="40" x2="86" y2="48"/>
      </g>
    </svg>
    <div class="cta-text">Try it Free Today!</div>
  </section>

  <footer class="band band--green footer"></footer>
</main>
</body>
</html>
```